Varnel Group Limited Stationary

We are in need of business card and letterhead designs. We are looking for clean modern designs that complement the style and feel of our logo.

```html
<!DOCTYPE html>
<html lang="en">
<head>
<meta charset="utf-8">
<title>Varnel Group Limited – Stationery</title>
<link rel="stylesheet" href="https://fonts.googleapis.com/css2?family=Mulish:wght@400;500;700&display=swap">
<style>
  :root {
    --navy: #0b2a5e;
    --royal: #1a4a8c;
    --mist: #d1d2d4;
    --ink: #1f2326;
    --paper: #ffffff;
    --frame: #8c8f92;
    --teal-rule: #6f9aa3;
  }
  * { box-sizing: border-box; margin: 0; padding: 0; }
  html, body { width: 1200px; height: 897px; overflow: hidden; background: var(--paper); }
  body { position: relative; font-family: "Mulish", Arial, sans-serif; color: var(--ink); }

  .sheet { position: absolute; background: var(--paper); border: 1px solid var(--frame); overflow: hidden; }

  .band { position: absolute; left: 0; right: 0; }
  .band.mist { background: var(--mist); }
  .band.royal { background: var(--royal); }
  .band.navy { background: var(--navy); }

  .mark-dot { position: absolute; border-radius: 50%; background: var(--royal); }
  .wordmark {
    position: absolute; font-family: "Mulish", Arial, sans-serif; font-weight: 700;
    color: var(--royal); white-space: nowrap; letter-spacing: 1px;
  }
  .rule { position: absolute; height: 1.5px;
    background: linear-gradient(90deg, rgba(26,74,140,0), var(--royal) 20%, var(--teal-rule) 70%, rgba(111,154,163,0)); }

  /* Letterhead */
  .letterhead { left: 18px; top: 9px; width: 650px; height: 842px; }
  .letterhead .mark-dot.top { left: 134px; top: 43px; width: 72px; height: 72px; }
  .letterhead .wordmark { left: 54px; top: 122px; font-size: 27px; }
  .letterhead .rule { left: 54px; top: 158px; width: 540px; }
  .contact-line {
    position: absolute; left: 65px; top: 170px; font-size: 12px; letter-spacing: 0.4px;
    display: flex; gap: 12px; white-space: nowrap; color: var(--ink);
  }
  .contact-line .sep { color: var(--royal); font-weight: 700; }
  .letterhead .mark-dot.foot { left: 287px; top: 710px; width: 52px; height: 52px; }
  .letterhead .band.mist { top: 772px; height: 22px; }
  .letterhead .band.royal { top: 794px; height: 5px; }
  .letterhead .band.navy { top: 799px; bottom: 0; }

  /* Business card – front */
  .card-front { left: 627px; top: 242px; width: 252px; height: 378px; box-shadow: 1px 2px 4px rgba(0,0,0,0.25); z-index: 2; }
  .card-front .mark-dot { left: 93px; top: 50px; width: 64px; height: 64px; }
  .card-front .wordmark { left: 0; right: 0; top: 124px; text-align: center; font-size: 23px; }
  .card-front .rule { left: 20px; top: 155px; width: 210px; }
  .tagline { position: absolute; left: 0; right: 0; top: 184px; text-align: center; font-size: 12px; line-height: 15px; color: var(--ink); }
  .card-front .band.mist { top: 240px; height: 18px; }
  .card-front .band.royal { top: 258px; height: 5px; }
  .card-front .band.navy { top: 263px; bottom: 0; }
  .web { position: absolute; left: 0; right: 0; top: 311px; text-align: center; color: var(--paper);
    font-size: 18px; font-weight: 700; letter-spacing: 1px; }

  /* Business card – back */
  .card-back { left: 818px; top: 526px; width: 377px; height: 219px; z-index: 1; }
  .card-back .mark-dot { left: 40px; top: 60px; width: 100px; height: 100px; }
  .person { position: absolute; left: 159px; top: 50px; font-size: 15px; line-height: 22px; letter-spacing: 0.4px; }
  .card-back .rule { left: 157px; top: 104px; width: 200px; }
  .reach { position: absolute; left: 159px; top: 117px; font-size: 15px; line-height: 22px; letter-spacing: 0.4px; }

  .caption { position: absolute; top: 886px; font-size: 11px; letter-spacing: 0.6px; color: var(--ink); }
</style>
</head>
<body>

<section class="sheet letterhead" aria-label="Letterhead">
  <div class="mark-dot top"></div>
  <div class="wordmark">VARNEL GROUP</div>
  <div class="rule"></div>
  <div class="contact-line">
    <span>1234 STREET NAME</span><span class="sep">|</span>
    <span>CITY, STATE 00000</span><span class="sep">|</span>
    <span>555.555.555</span><span class="sep">|</span>
    <span>EMAIL@EMAIL.COM</span>
  </div>
  <div class="mark-dot foot"></div>
  <div class="band mist"></div>
  <div class="band royal"></div>
  <div class="band navy"></div>
</section>

<section class="sheet card-back" aria-label="Business card back">
  <div class="mark-dot"></div>
  <div class="person">Alan Reyes<br>Account Manager</div>
  <div class="rule"></div>
  <div class="reach">555.555.5555<br>alanreyes@email.com</div>
</section>

<section class="sheet card-front" aria-label="Business card front">
  <div class="mark-dot"></div>
  <div class="wordmark">VARNEL GROUP</div>
  <div class="rule"></div>
  <p class="tagline">Transforming passion and<br>purpose into reality.</p>
  <div class="band mist"></div>
  <div class="band royal"></div>
  <div class="band navy"></div>
  <div class="web">VARNELGROUP.COM</div>
</section>

<div class="caption" style="left:18px;">LETTERHEAD</div>
<div class="caption" style="left:808px;">BUSINESS CARD</div>

</body>
</html>
```